Redesign our business card for more impact

We want to completely replace the back design of our card, and refresh or even change the front entirely. We are happy with our black Q7 logo and do not want to change it.
Our company address changed too. It is now 58 Corvallen, Irvine, CA 92741
Updates

It was reported by Sketch Harbor email today that the uploaded files didnt upload. I am trying again.

Target Market(s)

Architects and Building Owners (People making multi-million dollar decisions)

Industry/Entity Type

Consulting Engineering

Contact Information for Business Card

Contact info on the front. "wallpaper" design on back with tag line on the back "Engineering Your Future"

Font styles to use
Sans Serif

Requirements
Must have
• A vivid, modern, impactful ...but tasteful back of card design. It should communicate our premier status, but grab attention as innovative. DESIGN SHOULD BE ELEGANT AND NOT TOO BUSY.
Nice to have
• Repeating pattern, multi-color, something creative...
Should not have
• Anything that looks too playful or that we are not serious professionals. It should also not be too boring or conservative.

```html
<!DOCTYPE html>
<html lang="en">
<head>
<meta charset="utf-8">
<title>Q7 Engineering – Business Card</title>
<link rel="stylesheet" href="https://fonts.googleapis.com/css2?family=Montserrat:wght@400;500;600;700&display=swap">
<style>
  :root {
    --page: #ffffff;
    --card-front: #f7f4ee;
    --card-back: #e8e3dc;
    --ink: #333333;
    --gold: #a2783a;
    --pattern-line: #d3cec6;
  }
  * { margin: 0; padding: 0; box-sizing: border-box; }
  html, body {
    width: 1200px; height: 800px; overflow: hidden;
    background: var(--page);
    font-family: "Montserrat", sans-serif;
  }
  .canvas { position: relative; width: 1200px; height: 800px; }
  .card { position: absolute; top: 25px; width: 567px; height: 748px; }
  .card-front { left: 23px; background: var(--card-front); }
  .card-back { left: 609px; background: var(--card-back); overflow: hidden; }

  .wordmark {
    position: absolute; left: 84px; top: 110px;
    font-size: 112px; font-weight: 700; line-height: 1;
    color: var(--ink); letter-spacing: -2px;
  }
  .accent-rule {
    position: absolute; left: 86px; top: 261px;
    width: 60px; height: 2px; background: var(--gold);
  }
  .person-name {
    position: absolute; left: 86px; top: 310px;
    font-size: 28px; font-weight: 600; letter-spacing: 2.4px;
    color: var(--ink); white-space: nowrap;
  }
  .person-title {
    position: absolute; left: 86px; top: 350px;
    font-size: 17px; font-weight: 500; letter-spacing: 4px;
    color: var(--gold);
  }
  .contact-list {
    position: absolute; left: 86px; top: 420px;
    height: 203px; border-left: 2px solid var(--gold);
    list-style: none;
  }
  .contact-item {
    position: absolute; left: 0; display: flex; align-items: center;
    white-space: nowrap; font-size: 16.5px; color: var(--ink);
  }
  .contact-item svg {
    position: absolute; left: 16px; width: 28px; height: 28px;
    fill: none; stroke: var(--gold); stroke-width: 1.4;
    stroke-linecap: round; stroke-linejoin: round;
  }
  .contact-item span { position: absolute; left: 71px; }
  .contact-phone { top: 24px; }
  .contact-email { top: 75px; }
  .contact-web { top: 125px; }
  .contact-address { top: 178px; }

  .footer-line {
    position: absolute; left: 0; top: 702px;
    width: 492px; height: 1px; background: var(--gold);
  }
  .footer-ticks { position: absolute; left: 493px; top: 690px; display: flex; gap: 12px; }
  .footer-ticks i { display: block; width: 2px; height: 24px; background: var(--gold); }

  .back-pattern {
    position: absolute; inset: 0;
    background: linear-gradient(135deg, #ebe7e0 0%, #e4dfd7 50%, #ebe6df 100%);
  }
  .tagline {
    position: absolute; left: 92px; top: 360px;
    width: 372px; height: 42px;
    display: flex; align-items: center; justify-content: center;
    border-left: 2px solid var(--gold); border-right: 2px solid var(--gold);
    font-size: 20px; font-weight: 500; letter-spacing: 3.2px;
    color: var(--gold); white-space: nowrap;
  }
</style>
</head>
<body>
<div class="canvas">
  <section class="card card-front">
    <div class="wordmark">Q7</div>
    <div class="accent-rule"></div>
    <h1 class="person-name">DANIEL HARLOW</h1>
    <p class="person-title">PRINCIPAL ENGINEER</p>
    <ul class="contact-list">
      <li class="contact-item contact-phone">
        <svg viewBox="0 0 24 24"><path d="M6 3l3 4-2 2c1 3 4 6 7 7l2-2 4 3-2 3C10 20 4 14 3 5z"/></svg>
        <span>949.555.0382</span>
      </li>
      <li class="contact-item contact-email">
        <svg viewBox="0 0 24 24"><rect x="2" y="5" width="20" height="14"/><path d="M2 5l10 8 10-8"/></svg>
        <span>daniel.harlow@q7engineering.com</span>
      </li>
      <li class="contact-item contact-web">
        <svg viewBox="0 0 24 24"><circle cx="12" cy="12" r="10"/><ellipse cx="12" cy="12" rx="4.5" ry="10"/><path d="M2 12h20M4 7h16M4 17h16"/></svg>
        <span>q7engineering.com</span>
      </li>
      <li class="contact-item contact-address">
        <svg viewBox="0 0 24 24"><path d="M12 22s-7-7.5-7-13a7 7 0 0 1 14 0c0 5.5-7 13-7 13z"/><circle cx="12" cy="9" r="2.5"/></svg>
        <span>58 Corvallen, Irvine, CA 92741</span>
      </li>
    </ul>
    <div class="footer-line"></div>
    <div class="footer-ticks"><i></i><i></i><i></i></div>
  </section>

  <section class="card card-back">
    <div class="back-pattern" role="img" aria-label="Subtle geometric line wallpaper pattern of light grey angled and vertical lines"></div>
    <p class="tagline">Engineering Your Future</p>
  </section>
</div>
</body>
</html>
```